Lantern Business Cards

Need business cards for my employees at my restaurant.

Needs to include:
Our Logo
Lantern Bowls & Brews
Name: Nora Pettigrew
Title : Owner
Address: 487 Mirella Ave. Lake Havasu City, AZ 86519
Web: www.lanternkestrel.com
Phone: 928-555-0147
Cell: 928-555-0192
Email: info@lanternkestrel.com

```html
<!DOCTYPE html>
<html lang="en">
<head>
<meta charset="utf-8">
<title>Lantern Bowls &amp; Brews – Business Cards</title>
<link rel="stylesheet" href="https://fonts.googleapis.com/css2?family=Libre+Baskerville:wght@700&family=Montserrat:wght@400;500;700&display=swap">
<style>
  :root {
    --red: #c01f30;
    --black: #0b0b0c;
    --white: #ffffff;
    --ink: #1a1a1a;
    --backdrop: #cfcfcf;
  }
  * { box-sizing: border-box; margin: 0; padding: 0; }
  html, body {
    width: 1200px; height: 800px; overflow: hidden;
    background: var(--backdrop);
    font-family: "Montserrat", sans-serif;
  }
  .card {
    position: absolute;
    top: 245px;
    width: 540px; height: 309px;
    border-radius: 22px;
    border: 2px solid var(--red);
    overflow: hidden;
  }
  /* Front */
  .card--front { left: 40px; background: var(--white); }
  .corner-band {
    position: absolute; top: 0; right: 0;
    width: 130px; height: 48px; background: var(--red);
  }
  .contact-band {
    position: absolute; left: 0; top: 140px;
    width: 360px; height: 104px; background: var(--black);
  }
  .logo-disc {
    position: absolute; left: 320px; top: 42px;
    width: 190px; height: 190px; border-radius: 50%;
    background: var(--white);
    display: flex; align-items: center; justify-content: center;
  }
  .logo-name {
    font-weight: 700; font-size: 34px; color: var(--red);
    letter-spacing: 0.5px;
  }
  .person { position: absolute; left: 34px; top: 62px; }
  .person__name {
    font-family: "Libre Baskerville", serif; font-weight: 700;
    font-size: 21px; color: var(--red); text-transform: uppercase;
    letter-spacing: 0.5px;
  }
  .person__title { font-size: 15px; color: var(--ink); margin-top: 2px; }
  .contact-list {
    position: absolute; left: 34px; top: 152px;
    list-style: none; color: var(--white); font-size: 13px; line-height: 20px;
  }
  .contact-list li { display: flex; align-items: center; gap: 10px; }
  .contact-list svg { width: 12px; height: 12px; flex: none; }
  .contact-list .accent { color: var(--red); }
  .address {
    position: absolute; left: 34px; top: 256px;
    font-size: 13.5px; line-height: 19px; color: var(--ink);
  }
  /* Back */
  .card--back {
    left: 620px; background: var(--black);
    display: flex; align-items: center; justify-content: center; gap: 14px;
  }
  .back-mark { width: 46px; height: 46px; border-radius: 50%; background: var(--red); }
  .back-name { font-weight: 700; font-size: 27px; color: var(--red); }
</style>
</head>
<body>
  <section class="card card--front" aria-label="Business card front">
    <div class="corner-band"></div>
    <div class="contact-band"></div>
    <div class="logo-disc"><span class="logo-name">Lantern</span></div>

    <div class="person">
      <p class="person__name">Nora Pettigrew</p>
      <p class="person__title">Owner</p>
    </div>

    <ul class="contact-list">
      <li>
        <svg viewBox="0 0 12 12" aria-hidden="true"><path fill="#c01f30" d="M2.5 0.8l2 2.2-1 1.4a6 6 0 0 0 4.1 4.1l1.4-1 2.2 2-1.4 1.6C5.8 11 1 6.2 0.9 2.2z"/></svg>
        <span>928-555-0147</span>
      </li>
      <li>
        <svg viewBox="0 0 12 12" aria-hidden="true"><rect x="3" y="0.5" width="6" height="11" rx="1.2" fill="#c01f30"/><rect x="4" y="1.8" width="4" height="7" fill="#0b0b0c"/></svg>
        <span>928-555-0192</span>
      </li>
      <li>
        <svg viewBox="0 0 12 12" aria-hidden="true"><rect x="0.5" y="2" width="11" height="8" fill="#c01f30"/><path d="M0.5 2l5.5 4.5L11.5 2" stroke="#0b0b0c" fill="none"/></svg>
        <span>info@lanternkestrel.com</span>
      </li>
      <li>
        <svg viewBox="0 0 12 12" aria-hidden="true"><circle cx="6" cy="6" r="5.5" fill="#c01f30"/><path d="M0.5 6h11M6 0.5v11M2 3h8M2 9h8" stroke="#0b0b0c" stroke-width="0.8" fill="none"/></svg>
        <span>www.<span class="accent">lanternkestrel</span>.com</span>
      </li>
    </ul>

    <p class="address">487 Mirella Ave.<br>Lake Havasu City, AZ 86519</p>
  </section>

  <section class="card card--back" aria-label="Business card back">
    <div class="back-mark"></div>
    <span class="back-name">Lantern Bowls &amp; Brews</span>
  </section>
</body>
</html>
```